Flyer Needed to Advertise New Online Reading Programs

ABOUT THE TRUST OF READING DEVELOPMENT
The Trust teaches summer reading skills programs for elementary school students, in programs offered through partnerships with universities, colleges and municipalities nationwide. The goal of each program is to build reading skills, and to foster a lifetime love of books and reading.

AIMS & TARGET MARKET
The Trust has developed a new format of its’ online reading program for elementary students, which includes live small-group video classes taught by a professional reading teacher. The Trust seeks a new graphic design for a flyer to advertise the new online reading program. The flyer will be sent to elementary schools, passed out by teachers, and then taken home by students to show parents; therefore, the primary audience for the flyer will be teachers and parents of elementary school students.

Live classes for children are completely new in online education, unlike anything else in the marketplace, and parents and teachers therefore have no experience with them. The successful design will include illustrations or photographs that allow visitors to immediately grasp/understand the new video class format, without relying heavily on a written description. Additionally, the successful flyer concept will make the program, and the video classes in particular, feel fun and appealing to kids and parents.

Below is additional information about the new live small-group video class format, which meets weekly for 6 weeks:
o During video classes, students participate from home.
o During discussions, the student’s computer (or tablet) screen is filled with live video frames of the teacher and the other students. The video frame for the teacher is larger, and the other students appear in smaller frames.
o During other video class instruction, the teacher uses a presentation screen to display pages of a book or a “whiteboard” used for instructional activities.

Notes: The flyer design could include an illustrated or photo screenshot of a video class, with children looking engaged and a teacher leading them in discussion (stock photos are okay to use in flyer design). We have included a screen shot of one of these classes for reference, but do not feel constrained to represent this screen realistically (as shown here). Layout, look and feel can be changed. Alternatively, you may choose to use a graphic other than a screenshot to bring across the concept of the video classes.

COPY AND SPECIFICATIONS
The flyer design will be one-sided and the dimensions are 8.5” x 11” in either portrait or landscape orientation. We will consider designs in color or black and white. Since we brand our flyers with logos of the universities we partner with throughout the nation, we’ll need to include a partner logo in the design. Exact copy will be provided, but layout is flexible. Screenshots from our sample classes are included to show screen layout. Stock photos are okay to use in flyer designs.

Reason: We'd like to make edits to existing designs.

Hi designers, We wanted to share our thoughts on the main image of the flyer. We're leaning towards an image that shows a sole student on a computer with the computer screen in view. The computer screen could have the sample image we provided to show how the video classes operate. Thanks! The Trust of Reading Development

Graphic Design

```html
<!DOCTYPE html>
<html lang="en">
<head>
<meta charset="utf-8">
<title>Reading Skills Classes – Summer Flyer</title>
<link rel="stylesheet" href="https://fonts.googleapis.com/css2?family=Audiowide&family=PT+Sans:wght@400;700&family=PT+Sans+Narrow:wght@700&display=swap">
<style>
  :root {
    --backdrop-dark: #1a1a1a;
    --backdrop-light: #6a6a6a;
    --flyer-deep: #160507;
    --flyer-red: #5e0b12;
    --box-top: #7d0d15;
    --box-bottom: #240508;
    --accent-yellow: #f7ec12;
    --text-white: #ffffff;
    --screen-frame: #f2f2f2;
    --screen-dark: #1c2530;
  }
  * { box-sizing: border-box; margin: 0; padding: 0; }
  html, body { width: 999px; height: 1200px; overflow: hidden; }
  body {
    position: relative;
    background: radial-gradient(ellipse at center, var(--backdrop-light) 0%, var(--backdrop-dark) 75%);
    font-family: "PT Sans", sans-serif;
    color: var(--text-white);
  }
  .flyer {
    position: absolute; left: 58px; top: 35px; width: 884px; height: 1132px;
    background:
      radial-gradient(ellipse at 45% 45%, var(--flyer-red) 0%, rgba(94,11,18,0.5) 40%, transparent 75%),
      linear-gradient(180deg, #2a080b 0%, var(--flyer-deep) 100%);
    overflow: hidden;
  }
  .title-main {
    position: absolute; left: 26px; top: 26px;
    font-family: "Audiowide", sans-serif; font-weight: 400; font-size: 100px; line-height: 1;
    color: var(--accent-yellow); letter-spacing: 0;
    transform: scaleY(1.12); transform-origin: top left;
  }
  .title-sub {
    position: absolute; left: 27px; top: 142px;
    font-family: "Audiowide", sans-serif; font-size: 48px; line-height: 1;
    color: var(--accent-yellow); letter-spacing: 1px; word-spacing: 6px;
  }
  .tagline {
    position: absolute; left: 27px; top: 204px;
    font-size: 30px; line-height: 1; color: var(--text-white);
  }
  .class-screen {
    position: absolute; left: 538px; top: 39px; width: 316px; height: 212px;
    border: 4px solid var(--screen-frame); border-radius: 8px;
    background: linear-gradient(180deg, #c4b49a 0%, #6e6456 45%, var(--screen-dark) 60%, #0d1218 100%);
  }
  .feature-band {
    position: absolute; left: 0; top: 257px; width: 884px; height: 138px;
  }
  .feature-list {
    position: absolute; left: 37px; top: 267px; list-style: none;
    font-size: 23.5px; line-height: 29px;
  }
  .skill-list {
    position: absolute; left: 700px; top: 265px; list-style: none;
    font-size: 16px; line-height: 20.8px;
  }
  .feature-list li, .skill-list li { position: relative; padding-left: 22px; }
  .skill-list li { padding-left: 15px; }
  .feature-list li::before, .skill-list li::before {
    content: "•"; position: absolute; left: 0;
  }
  .program {
    position: absolute; padding: 6px 16px 0 16px;
    background: linear-gradient(180deg, var(--box-top) 0%, var(--box-bottom) 100%);
    border-radius: 3px;
  }
  .program h2 {
    font-family: "PT Sans Narrow", sans-serif; font-weight: 700;
    font-size: 22px; line-height: 1.1; color: var(--accent-yellow); margin-bottom: 4px;
  }
  .program p {
    font-size: 16.5px; line-height: 20.5px; text-align: justify;
  }
  .program--pre { left: 26px; top: 415px; width: 413px; height: 147px; }
  .program--k   { left: 467px; top: 415px; width: 386px; height: 147px; }
  .program--g1  { left: 26px; top: 572px; width: 413px; height: 146px; }
  .program--g2  { left: 467px; top: 572px; width: 386px; height: 146px; }
  .program--g3  { left: 26px; top: 729px; width: 413px; height: 140px; }
  .program--g45 { left: 467px; top: 729px; width: 386px; height: 140px; }
  .program--g45 p { font-size: 15.5px; letter-spacing: -0.4px; }
  .program--upper { left: 26px; top: 880px; width: 827px; height: 102px; }
  .program--upper p { text-align: left; font-size: 16.3px; }
  .hours {
    position: absolute; left: 0; top: 983px; width: 884px; text-align: center;
    font-size: 29px; color: var(--accent-yellow);
  }
  .footer-band {
    position: absolute; left: 0; top: 1024px; width: 884px; height: 108px;
    background: linear-gradient(180deg, #1e0507 0%, #3c070c 100%);
  }
  .partner {
    position: absolute; left: 32px; top: 1036px; display: flex; align-items: center; gap: 10px;
  }
  .partner-mark { width: 16px; height: 16px; background: var(--text-white); }
  .partner-name {
    font-size: 24px; line-height: 1.15; color: var(--text-white); letter-spacing: 1px;
  }
  .register-cta {
    position: absolute; left: 300px; top: 1024px; width: 560px; text-align: center;
  }
  .register-cta .lead { font-size: 34px; line-height: 1.2; }
  .register-cta .phone {
    font-weight: 700; font-size: 58px; line-height: 1.1; color: var(--accent-yellow);
  }
</style>
</head>
<body>
  <main class="flyer">
    <svg class="feature-band" viewBox="0 0 884 138" aria-hidden="true">
      <defs>
        <linearGradient id="bandFill" x1="0" y1="0" x2="1" y2="0">
          <stop offset="0" stop-color="#8a1019"/>
          <stop offset="0.7" stop-color="#5a0a10"/>
          <stop offset="1" stop-color="#2a0609"/>
        </linearGradient>
      </defs>
      <polygon points="0,0 600,0 640,138 0,138" fill="url(#bandFill)"/>
      <polygon points="600,0 884,0 884,138 640,138" fill="#2b070a" opacity="0.6"/>
    </svg>

    <h1 class="title-main">Reading</h1>
    <div class="title-sub">Skills Classes</div>
    <p class="tagline">Online this Summer!</p>

    <div class="class-screen" role="img" aria-label="Screenshot of a live online video class: a teacher wearing a headset in a large frame with small student video frames below"></div>

    <ul class="feature-list">
      <li>Small class size</li>
      <li>A skilled and encouraging teacher</li>
      <li>Individualized skills instruction</li>
      <li>A program of independent reading in great books</li>
    </ul>

    <ul class="skill-list">
      <li>Phonics</li>
      <li>Comprehension</li>
      <li>Fluency</li>
      <li>Study Skills</li>
      <li>Speed Reading</li>
      <li>Love of Reading</li>
    </ul>

    <section class="program program--pre">
      <h2>Program for Preschoolers:</h2>
      <p>Students in this program build strong reading readiness skills. Your child will learn letter recognition and beginning phonics, and develop the motivation and love of reading that make learning to read easy, enjoyable, and successful.</p>
    </section>
    <section class="program program--k">
      <h2>Program for Entering Kindergartners:</h2>
      <p>Students in this program learn beginning reading skills and develop a love of books. Your child will learn letter recognition, phonics, and sight words, and will learn to sound out short words.</p>
    </section>
    <section class="program program--g1">
      <h2>Program for Entering 1st Graders:</h2>
      <p>Students in this program learn to read independently. Your child will learn phonics and sight words, build comprehension, and gain the skills and confidence needed for success in first grade.</p>
    </section>
    <section class="program program--g2">
      <h2>Program for Entering 2nd Graders:</h2>
      <p>Students in this program become fluent, independent readers. Your child will make significant gains in phonics and word-attack skills, fluency, and comprehension, and will develop confidence and a love of reading.</p>
    </section>
    <section class="program program--g3">
      <h2>Program for Entering 3rd Graders:</h2>
      <p>Students in this program become strong independent readers. Your child will develop the comprehension, fluency, and long-word decoding skills needed to read longer books with ease, and will build confidence and a love of reading.</p>
    </section>
    <section class="program program--g45">
      <h2>Program for Entering 4th and 5th Graders:</h2>
      <p>Students in this program make substantial gains in comprehension, long-word decoding skills, fluency, and reading speed. Your child will complete homework more quickly and easily, be more successful in school, and become a strong, enthusiastic reader.</p>
    </section>
    <section class="program program--upper">
      <h2>Programs for Entering 6th-8th Graders and Entering 9th and 10th Graders:</h2>
      <p>Students in these programs make substantial gains in comprehension while doubling reading speed. They also learn the best way to read textbooks, take notes, and study for tests. As a result, students complete homework more quickly and easily, get better grades, and enjoy reading more.</p>
    </section>

    <p class="hours">Mon.-Fri. 5am–7pm, Sat. 5am–4pm and Sun. 6am–4pm</p>

    <div class="footer-band" aria-hidden="true"></div>
    <div class="partner">
      <span class="partner-mark" aria-hidden="true"></span>
      <span class="partner-name">NORTHBRIDGE<br>UNIVERSITY</span>
    </div>
    <div class="register-cta">
      <p class="lead">For More Information or to Register</p>
      <p class="phone">Call 1-800-555-0147</p>
    </div>
  </main>
</body>
</html>
```